Audira app for Android

We need design for Android application for selling audio lectures. The author of the lectures is a fairly well-known philologist and writer who has lectured on various topics (film, literature, etc.)

Design for the same iOS app has been succesfuly developed about nine month ago.

Design have to be developed for both tablet and phone in the "Matherial design" style and with colours as at existing app (see attachments).

There are 5 screens in this application.

1. Splash screen with application title "Vemra's library". This screen appears for 2-3 seconds at the app start.

2. Screen with a list of lectures. There must be the Author's photo (logo) and the app title in the screen as well as the list of lectures (starting from the last one) with pictures. The sketch in the attachment. Each lecture must have a category mark (movies, literature) as well as the title and a short description. In the list must be some difference between fully listened to lectures, thouse that haven't been listened to to the end. And thouse haven't been purchased yet. In the attached layout it is marked with the color of the ring next to each item. We need small palaying status at the bottom of the screen In the phone design (see attachment).
3. Player screen..It is desirable to see the progress of the lectures, title, lectures picture^ an opportunity to download it for listening offline, an icon to mark the lecture as the listened to, total duration and current position. .

4. Purchase screen

5. Info screen with some app settings (restore purchase, entering promo code and change a language).

The design should be in the "Material design" style and with colours as in the iOS app.

See existing iOS design in the files iOS4-iOS4.png

```html
<!DOCTYPE html>
<html lang="en">
<head>
<meta charset="utf-8">
<title>Audira – Lecture list</title>
<link rel="stylesheet" href="https://fonts.googleapis.com/css2?family=Roboto:wght@400;500;700&display=swap">
<style>
:root{
  --status:#f0541c;
  --primary:#ff5a1f;
  --accent:#ff5a3c;
  --accent-soft:#f7854f;
  --done:#7c8f45;
  --page:#eceef1;
  --white:#ffffff;
  --tab-dim:#ffc4ab;
  --text-grey:#a5a5a5;
  --text-dark:#3a3a3a;
  --track:#8c8c8c;
  --track-light:#c9c9c9;
}
*{box-sizing:border-box;margin:0;padding:0}
html,body{width:675px;height:1200px;overflow:hidden;background:var(--page);font-family:'Roboto',sans-serif}
.screen{position:relative;width:675px;height:1200px;overflow:hidden;background:var(--page)}
.status-bar{position:absolute;left:0;top:0;width:675px;height:45px;background:var(--status)}
.status-bar .clock{position:absolute;right:16px;top:10px;color:var(--white);font-size:22px}
.status-bar svg{position:absolute;top:11px}
.app-bar{position:absolute;left:0;top:45px;width:675px;height:192px;background:var(--primary)}
.app-bar .menu-btn{position:absolute;left:35px;top:37px}
.app-bar .title{position:absolute;left:141px;top:26px;color:var(--white);font-size:35px;font-weight:400}
.app-bar .more-btn{position:absolute;left:624px;top:33px}
.tabs{position:absolute;left:0;top:103px;width:675px;height:89px}
.tab{position:absolute;top:30px;font-size:21px;font-weight:500;color:var(--tab-dim);transform:translateX(-50%)}
.tab.active{color:var(--white)}
.tab-indicator{position:absolute;left:0;bottom:0;width:225px;height:6px;background:var(--white)}
.author-row{position:absolute;left:0;top:237px;width:675px;height:113px;background:var(--white);box-shadow:0 1px 3px rgba(0,0,0,.15)}
.author-photo{position:absolute;left:0;top:3px;width:110px;height:107px;background:linear-gradient(160deg,#9aa6ad,#3a3f44 70%,#1f2226)}
.author-name{position:absolute;left:261px;top:38px;font-size:28px;color:var(--text-grey)}
.card{position:absolute;width:305px;height:353px;border-radius:3px;overflow:hidden;box-shadow:0 1px 4px rgba(0,0,0,.3);color:var(--white)}
.card .art{position:absolute;inset:0}
.card .shade{position:absolute;left:0;right:0;top:225px;bottom:0;background:rgba(40,40,40,.55)}
.card .c-title{position:absolute;right:14px;top:10px;font-size:22px;font-weight:700}
.card .c-cat{position:absolute;right:14px;top:53px;font-size:16px;color:var(--accent-soft)}
.card .action{position:absolute;left:18px;top:64px;width:82px;height:82px;border-radius:50%;display:flex;align-items:center;justify-content:center;box-shadow:0 2px 4px rgba(0,0,0,.3)}
.action.play{background:var(--accent)}
.action.buy{background:var(--accent-soft)}
.action.done{background:var(--done)}
.card .duration{position:absolute;left:10px;top:176px;display:flex;align-items:center;gap:10px;font-size:15px}
.card .dl{position:absolute;right:14px;top:174px}
.card .track{position:absolute;left:0;right:0;top:207px;height:19px;background:rgba(180,180,180,.55)}
.card .track .fill{position:absolute;left:0;top:0;bottom:0}
.card .desc{position:absolute;left:14px;right:10px;top:240px;font-size:17px;line-height:23px}
.c1{left:16px;top:366px}.c2{left:352px;top:366px}.c3{left:16px;top:756px}.c4{left:352px;top:756px}
.c1 .art{background:linear-gradient(180deg,#8d8d8d,#5c5c5c)}
.c2 .art{background:linear-gradient(180deg,#6a6a6a,#3e3e3e)}
.c3 .art{background:linear-gradient(160deg,#a9a290,#6d6a60)}
.c4 .art{background:linear-gradient(180deg,#4b4f7d,#2e3356 60%,#4e4a52)}
.overflow-menu{position:absolute;left:383px;top:144px;width:270px;height:281px;background:var(--white);border-radius:2px;box-shadow:0 4px 12px rgba(0,0,0,.3)}
.menu-item{height:71px;display:flex;align-items:center;padding-left:24px;gap:24px;font-size:24px;color:var(--text-dark);border-bottom:1px solid #e3e3e3}
.menu-item:last-child{border-bottom:none}
.mini-player{position:absolute;left:0;top:1085px;width:675px;height:115px;background:var(--white);box-shadow:0 -2px 6px rgba(0,0,0,.15)}
.mini-player .pause{position:absolute;left:22px;top:37px}
.mini-player .elapsed{position:absolute;left:80px;top:50px;font-size:15px;color:var(--text-dark)}
.mini-player .np-title{position:absolute;left:0;width:670px;top:11px;text-align:center;font-size:15px;color:var(--text-dark)}
.mini-player .np-author{position:absolute;left:0;width:670px;top:33px;text-align:center;font-size:11px;color:var(--accent)}
.mini-player .np-cat{position:absolute;left:0;width:670px;top:77px;text-align:center;font-size:12px;color:var(--accent)}
.mini-player .bar{position:absolute;left:141px;top:51px;width:382px;height:15px;background:#555;border-radius:3px;overflow:hidden}
.mini-player .bar .fill{position:absolute;left:0;top:0;bottom:0;width:312px;background:var(--accent)}
.mini-player .bar .thumb{position:absolute;left:312px;top:0;bottom:0;width:6px;background:var(--white)}
.mini-player .remain{position:absolute;left:544px;top:50px;font-size:15px;color:var(--accent)}
.mini-player .dl{position:absolute;left:615px;top:40px}
</style>
</head>
<body>
<div class="screen">
  <div class="status-bar">
    <svg style="left:525px" width="22" height="22" viewBox="0 0 22 22"><path d="M22 0V22H0Z" fill="#fff" opacity=".5"/><path d="M14 8V22H0Z" fill="#fff"/></svg>
    <svg style="left:563px" width="14" height="24" viewBox="0 0 14 24"><rect x="4" y="0" width="6" height="3" fill="#fff"/><rect x="0" y="3" width="14" height="21" rx="1" fill="#fff" opacity=".5"/><rect x="0" y="11" width="14" height="13" rx="1" fill="#fff"/></svg>
    <span class="clock">12:30</span>
  </div>

  <header class="app-bar">
    <svg class="menu-btn" width="34" height="24" viewBox="0 0 34 24"><rect y="0" width="34" height="4" fill="#fff"/><rect y="10" width="34" height="4" fill="#fff"/><rect y="20" width="34" height="4" fill="#fff"/></svg>
    <h1 class="title">Audira</h1>
    <svg class="more-btn" width="14" height="36" viewBox="0 0 14 36"><circle cx="7" cy="5" r="4" fill="#fff"/><circle cx="7" cy="18" r="4" fill="#fff"/><circle cx="7" cy="31" r="4" fill="#fff"/></svg>
    <nav class="tabs">
      <span class="tab active" style="left:112px">ALL</span>
      <span class="tab" style="left:335px">MOVIES</span>
      <span class="tab" style="left:560px">LITERATURE</span>
      <span class="tab-indicator"></span>
    </nav>
  </header>

  <section class="author-row">
    <div class="author-photo" role="img" aria-label="Portrait photo of the lecturer"></div>
    <span class="author-name">Marten Holloway</span>
  </section>

  <article class="card c1">
    <div class="art" role="img" aria-label="Engraved portrait of a nineteenth-century poet"></div>
    <div class="shade"></div>
    <h2 class="c-title">The Nature of Creativity</h2>
    <span class="c-cat">Philosophy</span>
    <div class="action play"><svg width="26" height="30" viewBox="0 0 26 30"><path d="M2 0L26 15L2 30Z" fill="#fff"/></svg></div>
    <div class="duration"><svg width="20" height="20" viewBox="0 0 20 20"><circle cx="10" cy="10" r="8.5" fill="none" stroke="#fff" stroke-width="2"/><path d="M10 5V10H14" fill="none" stroke="#fff" stroke-width="2"/></svg>1h 35min</div>
    <svg class="dl" width="20" height="20" viewBox="0 0 20 20"><path d="M7 0H13V7H18L10 15L2 7H7Z" fill="#eee"/><rect y="17" width="20" height="3" fill="#eee"/></svg>
    <div class="track"><span class="fill" style="width:176px;background:var(--accent)"></span><span class="fill" style="left:172px;width:8px;background:#fff"></span></div>
    <p class="desc">This course is an introduction to problems about creativity as it pervades human experience and behavior.</p>
  </article>

  <article class="card c2">
    <div class="art" role="img" aria-label="Photographic portrait of a bearded writer"></div>
    <div class="shade"></div>
    <h2 class="c-title">The Nature of Creativity</h2>
    <span class="c-cat">Philosophy</span>
    <div class="action buy"><svg width="30" height="32" viewBox="0 0 30 32"><path d="M9 10V7A6 6 0 0 1 21 7V10" fill="none" stroke="#fff" stroke-width="2.5"/><rect x="2" y="10" width="26" height="22" rx="2" fill="#fff"/></svg></div>
    <div class="duration"><svg width="20" height="20" viewBox="0 0 20 20"><circle cx="10" cy="10" r="8.5" fill="none" stroke="#fff" stroke-width="2"/><path d="M10 5V10H14" fill="none" stroke="#fff" stroke-width="2"/></svg>1h 35min</div>
    <svg class="dl" width="20" height="20" viewBox="0 0 20 20"><path d="M7 0H13V7H18L10 15L2 7H7Z" fill="#999"/><rect y="17" width="20" height="3" fill="#999"/></svg>
    <div class="track"></div>
    <p class="desc">This course is an introduction to problems about creativity as it pervades human experience and behavior.</p>
  </article>

  <article class="card c3">
    <div class="art" role="img" aria-label="Illustration of a quill feather and inkwell"></div>
    <div class="shade"></div>
    <h2 class="c-title">The Nature of Creativity</h2>
    <span class="c-cat">Philosophy</span>
    <div class="action done"><svg width="30" height="24" viewBox="0 0 30 24"><path d="M3 12L11 20L27 4" fill="none" stroke="#fff" stroke-width="4"/></svg></div>
    <div class="duration"><svg width="20" height="20" viewBox="0 0 20 20"><circle cx="10" cy="10" r="8.5" fill="none" stroke="#fff" stroke-width="2"/><path d="M10 5V10H14" fill="none" stroke="#fff" stroke-width="2"/></svg>1h 35min</div>
    <svg class="dl" width="20" height="20" viewBox="0 0 20 20"><path d="M7 0H13V7H18L10 15L2 7H7Z" fill="#eee"/><rect y="17" width="20" height="3" fill="#eee"/></svg>
    <div class="track"><span class="fill" style="width:100%;background:var(--done)"></span></div>
    <p class="desc">This course is an introduction to problems about creativity as it pervades human experience and behavior.</p>
  </article>

  <article class="card c4">
    <div class="art" role="img" aria-label="Photo of a statue in front of a tall building at dusk"></div>
    <div class="shade"></div>
    <h2 class="c-title">The Nature of Creativity</h2>
    <span class="c-cat">Philosophy</span>
    <div class="action buy"><svg width="30" height="32" viewBox="0 0 30 32"><path d="M9 10V7A6 6 0 0 1 21 7V10" fill="none" stroke="#fff" stroke-width="2.5"/><rect x="2" y="10" width="26" height="22" rx="2" fill="#fff"/></svg></div>
    <div class="duration"><svg width="20" height="20" viewBox="0 0 20 20"><circle cx="10" cy="10" r="8.5" fill="none" stroke="#fff" stroke-width="2"/><path d="M10 5V10H14" fill="none" stroke="#fff" stroke-width="2"/></svg>1h 35min</div>
    <svg class="dl" width="20" height="20" viewBox="0 0 20 20"><path d="M7 0H13V7H18L10 15L2 7H7Z" fill="#999"/><rect y="17" width="20" height="3" fill="#999"/></svg>
    <div class="track"></div>
    <p class="desc">This course is an introduction to problems about creativity as it pervades human experience and behavior.</p>
  </article>

  <div class="overflow-menu">
    <div class="menu-item"><svg width="18" height="20" viewBox="0 0 18 20"><path d="M0 0L18 10L0 20Z" fill="#444"/></svg>Now Playing</div>
    <div class="menu-item"><svg width="18" height="18" viewBox="0 0 18 18"><circle cx="9" cy="9" r="9" fill="#444"/><rect x="4" y="7.5" width="10" height="3" fill="#fff"/></svg>Clear Queue</div>
    <div class="menu-item"><svg width="18" height="18" viewBox="0 0 18 18"><circle cx="9" cy="9" r="9" fill="#444"/><text x="9" y="14" text-anchor="middle" font-family="Roboto,sans-serif" font-weight="700" font-size="13" fill="#fff">?</text></svg>Help</div>
    <div class="menu-item"><svg width="18" height="18" viewBox="0 0 18 18"><circle cx="9" cy="9" r="9" fill="#444"/><rect x="7.7" y="7.5" width="2.6" height="7" fill="#fff"/><rect x="7.7" y="3.5" width="2.6" height="2.6" fill="#fff"/></svg>About</div>
  </div>

  <footer class="mini-player">
    <svg class="pause" width="34" height="43" viewBox="0 0 34 43"><rect width="11" height="43" rx="2" fill="#333"/><rect x="23" width="11" height="43" rx="2" fill="#333"/></svg>
    <span class="elapsed">-59:58</span>
    <span class="np-title">Philosophy of Love in the Western World</span>
    <span class="np-author">by Irene Dalvik</span>
    <div class="bar"><span class="fill"></span><span class="thumb"></span></div>
    <span class="remain">35:02</span>
    <span class="np-cat">Lectures | Philosophy</span>
    <svg class="dl" width="38" height="38" viewBox="0 0 38 38"><path d="M13 0H25V14H34L19 29L4 14H13Z" fill="#ff5a3c"/><rect y="33" width="38" height="5" fill="#ff5a3c"/></svg>
  </footer>
</div>
</body>
</html>
```